Monument sign* - Law Firm

*I am installing a monument sign that has LED, as well as backlit elements. I am seeking help in designing the backlit portion of the sign. The Backlit sign will be 12’ x 4’.

We are looking for a classic, yet eye-catching sign to help new and current clients find our firm as well as bring in future clients. One of our goals is that people who drive by on a regular basis remember our sign (and us) for any future legal need.

Target Market(s)

Current and future clientele

Industry/Entity Type

Law Firm

Font styles to use
Serif
Sans Serif

Colors
b1b1b1
333333

Requirements
Must have
• Business name: Hargrove Law Firm, Inc.
• Website: www.hargrovelawfirm-example.com
• Telephone: (555)214-3679
• Our firm's logo
Nice to have
• Color preference is black, taupe, and white. A photo for reference of the office coloring is uploaded.
• We currently have an established logo which our firm has been using for more than 10 years. Our logo has been used in advertising, commercials, letterhead, and on-site. We are looking to transition from brown/rust/cream to the black/taupe/white color scheme.
Should not have
• Cheesy slogans; character designs; directions; additional symbols outside of the firm's logo.

```html
<!DOCTYPE html>
<html lang="en">
<head>
<meta charset="utf-8">
<title>Hargrove Law Firm, Inc. – Monument Sign, Option 1</title>
<link rel="stylesheet" href="https://fonts.googleapis.com/css2?family=Arimo:wght@400&family=Poppins:wght@200&display=swap">
<style>
  :root {
    --page-bg: #f1f1f1;
    --sign-bg: #343233;
    --sign-text: #ffffff;
    --label-text: #6e6e6e;
    --caption-text: #333333;
    --shadow: rgba(0, 0, 0, 0.28);
  }
  * { margin: 0; padding: 0; box-sizing: border-box; }
  html, body {
    width: 1200px;
    height: 560px;
    overflow: hidden;
    background: var(--page-bg);
  }
  .canvas {
    position: relative;
    width: 1200px;
    height: 560px;
  }
  .option-label {
    position: absolute;
    top: 26px;
    right: 34px;
    font-family: "Poppins", sans-serif;
    font-weight: 200;
    font-size: 26px;
    color: var(--label-text);
  }
  .size-note {
    position: absolute;
    top: 93px;
    left: 120px;
    font-family: "Arimo", sans-serif;
    font-size: 8px;
    color: var(--caption-text);
  }
  .sign {
    position: absolute;
    left: 120px;
    top: 120px;
    width: 960px;
    height: 320px;
    background: var(--sign-bg);
    box-shadow: 14px 26px 22px var(--shadow);
    font-family: "Arimo", sans-serif;
    color: var(--sign-text);
  }
  .firm-mark {
    position: absolute;
    left: 49px;
    top: 69px;
    display: flex;
    align-items: center;
    gap: 10px;
  }
  .firm-mark__square {
    width: 180px;
    height: 180px;
    background: var(--sign-text);
  }
  .firm-mark__name {
    writing-mode: vertical-rl;
    font-size: 24px;
    letter-spacing: 8px;
    line-height: 1;
    color: var(--sign-text);
  }
  .sign-copy {
    position: absolute;
    left: 336px;
    top: 132px;
  }
  .firm-name {
    font-size: 38px;
    font-weight: 400;
    line-height: 1;
    letter-spacing: 0.3px;
    white-space: nowrap;
  }
  .contact-line {
    display: flex;
    align-items: center;
    gap: 34px;
    margin-top: 22px;
    font-size: 19px;
    line-height: 1;
    white-space: nowrap;
  }
  .contact-line__divider {
    width: 1.5px;
    height: 16px;
    background: var(--sign-text);
  }
</style>
</head>
<body>
  <div class="canvas">
    <p class="option-label">Option 1</p>
    <p class="size-note">Size -12' x 4'</p>

    <section class="sign" aria-label="Backlit monument sign panel">
      <div class="firm-mark">
        <div class="firm-mark__square"></div>
        <span class="firm-mark__name">HARGROVE</span>
      </div>

      <div class="sign-copy">
        <h1 class="firm-name">HARGROVE LAW FIRM, INC.</h1>
        <p class="contact-line">
          <span class="contact-line__phone">(555)214-3679</span>
          <span class="contact-line__divider" aria-hidden="true"></span>
          <span class="contact-line__web">www.hargrovelawfirm-example.com</span>
        </p>
      </div>
    </section>
  </div>
</body>
</html>
```